A Leisure SPA Plaza Hotel needs Creative VIP Cards Design

We need VIP Cards Design for a SPA Plaza Hotel, This leisure SPA plaza hotel have multiple sub projects, such as leisure hotel room, large buffet restaurant, swimming pool, theatrical performances, sauna bath, massage, SPA, Tea bar, 3D cinema, KTV rooms, chess room, Internet cafes , art appreciation, children's Castle, Korean geothermal, table tennis, billiard room, GYM and other entertainments.
We need Three creative VIP Card design for 3 different level:
1. Golden Card
2. Platinum Card
3. Diamond Card
Attached, Please find the LOGO file and some sample, we new design with much better look than those samples.

```html
<!DOCTYPE html>
<html lang="en">
<head>
<meta charset="utf-8">
<title>Sunmere Resort Club – VIP Cards</title>
<link rel="stylesheet" href="https://fonts.googleapis.com/css2?family=Cinzel:wght@700&family=Quicksand:wght@500&display=swap">
<style>
  :root{
    --page:#ececec;
    --onyx-top:#7b7b82;
    --onyx-top-dark:#4a4a50;
    --onyx-sparkle:#1b1b1d;
    --onyx-gem:#1c78c4;
    --onyx-gem-dark:#0b2f6a;
    --gold-light:#f8d77d;
    --gold-mid:#eab54a;
    --gold-deep:#c98a22;
    --gold-line:#c46d12;
    --plat-top:#e6e6ec;
    --plat-top-dark:#b9b9c2;
    --plat-sparkle:#c9c9cd;
    --plat-gem:#d7c9e2;
    --plat-gem-dark:#9d8dab;
    --band-light:#f2f2f4;
    --band-dark:#7d7d84;
    --stud:#f4f1f8;
    --ink:#141414;
    --white:#f4f4f6;
  }
  *{margin:0;padding:0;box-sizing:border-box}
  html,body{width:1200px;height:954px;overflow:hidden;background:var(--page)}
  .stage{position:relative;width:1200px;height:954px}
  .card{
    position:absolute;width:540px;height:340px;border-radius:22px;overflow:hidden;
    box-shadow:0 10px 24px rgba(0,0,0,.25);
  }
  .card svg{position:absolute;inset:0;width:100%;height:100%}
  .card--gold{left:570px;top:88px;z-index:1}
  .card--platinum{left:450px;top:498px;z-index:2}
  .card--diamond{left:98px;top:212px;z-index:3}
  .brand-dot{
    position:absolute;left:248px;top:46px;width:44px;height:44px;border-radius:50%;
  }
  .brand{
    position:absolute;left:0;right:0;top:102px;text-align:center;
    font-family:"Quicksand",sans-serif;font-weight:500;font-size:26px;line-height:32px;letter-spacing:.5px;
  }
  .tier{
    position:absolute;left:0;right:0;top:234px;text-align:center;
    font-family:"Cinzel",serif;font-weight:700;font-size:86px;line-height:1;letter-spacing:4px;
  }
  .card--gold .tier{top:212px}
  .card--diamond .brand{color:var(--white)}
  .card--diamond .brand-dot{background:var(--white)}
  .card--diamond .tier{color:var(--white);text-shadow:0 2px 3px rgba(0,0,0,.5)}
  .card--gold .brand,.card--platinum .brand{color:var(--ink)}
  .card--gold .brand-dot,.card--platinum .brand-dot{background:var(--ink)}
  .card--gold .tier,.card--platinum .tier{color:var(--ink);text-shadow:0 2px 3px rgba(0,0,0,.25)}
</style>
</head>
<body>
<main class="stage">

  <section class="card card--gold" aria-label="Golden VIP card">
    <svg viewBox="0 0 540 340" aria-hidden="true">
      <defs>
        <linearGradient id="goldFace" x1="0" y1="0" x2="1" y2="1">
          <stop offset="0" stop-color="var(--gold-light)"/>
          <stop offset=".55" stop-color="var(--gold-mid)"/>
          <stop offset="1" stop-color="var(--gold-deep)"/>
        </linearGradient>
        <radialGradient id="goldGem" cx=".5" cy=".4" r=".6">
          <stop offset="0" stop-color="var(--gold-light)"/>
          <stop offset="1" stop-color="var(--gold-deep)"/>
        </radialGradient>
      </defs>
      <rect width="540" height="340" fill="url(#goldFace)" role="img" aria-label="Faceted gold background"/>
      <circle cx="270" cy="350" r="130" fill="url(#goldGem)" stroke="var(--gold-light)" stroke-width="6" role="img" aria-label="Large cut gemstone in gold tones"/>
      <path d="M0 70 Q270 330 540 70" fill="none" stroke="var(--gold-line)" stroke-width="4"/>
      <g fill="var(--stud)" stroke="var(--band-dark)" stroke-width="1">
        <circle cx="43" cy="98" r="5"/><circle cx="108" cy="142" r="6"/><circle cx="173" cy="172" r="7"/>
        <circle cx="367" cy="172" r="7"/><circle cx="432" cy="142" r="6"/><circle cx="497" cy="98" r="5"/>
      </g>
    </svg>
    <span class="brand-dot" aria-hidden="true"></span>
    <p class="brand">Sunmere Resort Club</p>
    <p class="tier">VIP</p>
  </section>

  <section class="card card--platinum" aria-label="Platinum VIP card">
    <svg viewBox="0 0 540 340" aria-hidden="true">
      <defs>
        <linearGradient id="platFace" x1="0" y1="0" x2="1" y2="1">
          <stop offset="0" stop-color="var(--plat-top-dark)"/>
          <stop offset=".5" stop-color="var(--plat-top)"/>
          <stop offset="1" stop-color="var(--plat-top-dark)"/>
        </linearGradient>
        <linearGradient id="platBand" x1="0" y1="0" x2="0" y2="1">
          <stop offset="0" stop-color="var(--band-light)"/>
          <stop offset="1" stop-color="var(--band-dark)"/>
        </linearGradient>
        <radialGradient id="platGem" cx=".5" cy=".4" r=".6">
          <stop offset="0" stop-color="var(--plat-gem)"/>
          <stop offset="1" stop-color="var(--plat-gem-dark)"/>
        </radialGradient>
      </defs>
      <rect width="540" height="340" fill="var(--plat-sparkle)" role="img" aria-label="Silver glitter texture"/>
      <path d="M0 0 H540 V70 Q270 330 0 70 Z" fill="url(#platFace)" role="img" aria-label="Faceted pale silver panel"/>
      <circle cx="270" cy="350" r="120" fill="url(#platGem)" stroke="var(--band-light)" stroke-width="8" role="img" aria-label="Large cut gemstone in lavender silver"/>
      <path d="M0 70 Q270 330 540 70" fill="none" stroke="url(#platBand)" stroke-width="30"/>
      <g fill="var(--stud)" stroke="var(--band-dark)" stroke-width="1">
        <circle cx="43" cy="108" r="5"/><circle cx="108" cy="153" r="6"/><circle cx="173" cy="183" r="7"/>
        <circle cx="270" cy="200" r="7"/>
        <circle cx="367" cy="183" r="7"/><circle cx="432" cy="153" r="6"/><circle cx="497" cy="108" r="5"/>
      </g>
    </svg>
    <span class="brand-dot" aria-hidden="true"></span>
    <p class="brand">Sunmere Resort Club</p>
    <p class="tier">VIP</p>
  </section>

  <section class="card card--diamond" aria-label="Diamond VIP card">
    <svg viewBox="0 0 540 340" aria-hidden="true">
      <defs>
        <linearGradient id="onyxFace" x1="0" y1="0" x2="1" y2="1">
          <stop offset="0" stop-color="var(--onyx-top-dark)"/>
          <stop offset=".5" stop-color="var(--onyx-top)"/>
          <stop offset="1" stop-color="var(--onyx-top-dark)"/>
        </linearGradient>
        <linearGradient id="onyxBand" x1="0" y1="0" x2="0" y2="1">
          <stop offset="0" stop-color="var(--band-light)"/>
          <stop offset="1" stop-color="var(--band-dark)"/>
        </linearGradient>
        <radialGradient id="onyxGem" cx=".5" cy=".4" r=".6">
          <stop offset="0" stop-color="var(--onyx-gem)"/>
          <stop offset="1" stop-color="var(--onyx-gem-dark)"/>
        </radialGradient>
      </defs>
      <rect width="540" height="340" fill="var(--onyx-sparkle)" role="img" aria-label="Black glitter texture"/>
      <path d="M0 0 H540 V70 Q270 330 0 70 Z" fill="url(#onyxFace)" role="img" aria-label="Faceted graphite panel"/>
      <circle cx="270" cy="350" r="120" fill="url(#onyxGem)" stroke="var(--band-light)" stroke-width="8" role="img" aria-label="Large cut blue diamond"/>
      <path d="M0 70 Q270 330 540 70" fill="none" stroke="url(#onyxBand)" stroke-width="30"/>
      <g fill="var(--stud)" stroke="var(--band-dark)" stroke-width="1">
        <circle cx="43" cy="108" r="5"/><circle cx="108" cy="153" r="6"/><circle cx="173" cy="183" r="7"/>
        <circle cx="270" cy="200" r="7"/>
        <circle cx="367" cy="183" r="7"/><circle cx="432" cy="153" r="6"/><circle cx="497" cy="108" r="5"/>
      </g>
    </svg>
    <span class="brand-dot" aria-hidden="true"></span>
    <p class="brand">Sunmere Resort Club</p>
    <p class="tier">VIP</p>
  </section>

</main>
</body>
</html>
```